Brisk Chill Line Card

Vibrant Flyer - front and back (line card) with text and collage of pictures. Please include bleed lines. If same picture, use the best of available. Please do not duplicate.

Also include text:
(telephone no.) 888-472-1086
(web address) MobileBreezeandVolt.com
Rental Sales Service

Target Market(s)

Purchasers of equipment specific to market.

Font styles to use
Sans Serif

Colors
3277b5
fbed22
ec1f27

```html
<!DOCTYPE html>
<html lang="en">
<head>
<meta charset="utf-8">
<title>Brisk Chill Line Card</title>
<link href="https://fonts.googleapis.com/css2?family=Dosis:wght@500;600;700&family=Source+Sans+3:wght@400;600;700&display=swap" rel="stylesheet">
<style>
  :root{
    --blue:#3277b5;
    --blue-deep:#1f4f9a;
    --yellow:#fbed22;
    --red:#ec1f27;
    --red-deep:#c8161d;
    --ink:#1b1b1b;
    --paper:#f4f4f4;
    --stage:#e6e6e6;
  }
  *{box-sizing:border-box;margin:0;padding:0}
  html,body{width:1200px;height:889px;overflow:hidden;background:var(--stage)}
  body{position:relative;font-family:"Source Sans 3",Arial,sans-serif;color:var(--ink)}
  .sheet{position:absolute;top:177px;width:499px;height:645px;background:var(--paper);overflow:hidden;box-shadow:0 4px 14px rgba(0,0,0,.25)}
  .sheet--front{left:55px}
  .sheet--back{left:599px}
  .art{position:absolute;left:0;top:0}

  .brand{position:absolute;display:flex;align-items:center;gap:8px;color:var(--red);font-family:"Dosis",sans-serif;font-weight:600;font-size:22px;line-height:.95}
  .brand__dot{width:46px;height:46px;border-radius:50%;background:var(--red);flex:none}
  .tagline{position:absolute;text-align:right;font-family:"Dosis",sans-serif}
  .tagline__services{font-size:17px;font-weight:600;color:var(--ink)}
  .tagline__url{font-family:"Source Sans 3",sans-serif;font-size:10px;font-weight:700;color:var(--red);margin-top:2px}

  .photo{position:absolute;border:2px solid #fff;box-shadow:0 1px 3px rgba(0,0,0,.3)}
  .photo--crates{background:linear-gradient(160deg,#6b5a3c,#3d3427 60%,#8a7a5c)}
  .photo--trailer{background:linear-gradient(100deg,#d9a394 0 55%,#8c2f2c 55% 100%)}
  .photo--dock{background:linear-gradient(90deg,#9b3a34,#d6c7bd 45%,#5b4a3e)}
  .photo--hose{background:linear-gradient(170deg,#3b342c,#7c6c55 60%,#3a4b3a)}
  .photo--carrots{background:linear-gradient(180deg,#5a4a44,#e0553a 35%,#c23b25 80%,#6a3a30)}
  .photo--load{background:linear-gradient(90deg,#6a4b37,#b5784f 30%,#5b5a55 50%,#b5784f 70%,#6a4b37)}
  .equip{position:absolute}
  .equip--chiller{background:linear-gradient(180deg,#c8b23c,#e8d52a 40%,#3d3d3d 92%)}
  .equip--trailer{background:linear-gradient(180deg,#f1e22c,#e3d020 70%,#2b2b2b 92%)}

  .tab{position:absolute;height:26px;background:var(--blue);color:#fff;font-family:"Dosis",sans-serif;font-weight:600;font-size:19px;line-height:26px;padding-left:20px;border-radius:0 13px 13px 0;box-shadow:2px 2px 0 rgba(0,0,0,.25)}

  .bullets{position:absolute;list-style:none;font-size:8.3px;line-height:1.25}
  .bullets li{position:relative;padding-left:14px;margin-bottom:10px;text-align:justify}
  .bullets li::before{content:"";position:absolute;left:0;top:1px;width:8px;height:8px;border-radius:50%;background:var(--blue)}
  .bullets li::after{content:"";position:absolute;left:2.5px;top:3px;width:2.5px;height:2.5px;border-right:1.2px solid #fff;border-top:1.2px solid #fff;transform:rotate(45deg)}
  .bullets--light{color:#fff;font-size:7.9px}
  .bullets--light li{margin-bottom:11px}
  .bullets--light li::before{background:#fff}
  .bullets--light li::after{border-color:var(--red)}

  .panel{position:absolute;z-index:2;background:linear-gradient(160deg,var(--blue),var(--blue-deep));border:3px solid #fff;border-radius:12px;box-shadow:0 1px 4px rgba(0,0,0,.35)}
  .checks{list-style:none;color:#fff;font-weight:600}
  .checks li{position:relative;padding-left:16px}
  .checks li::before{content:"";position:absolute;left:0;top:2px;width:9px;height:9px;background:var(--yellow)}
  .checks li::after{content:"";position:absolute;left:2.5px;top:3.5px;width:3px;height:5px;border-right:1.5px solid var(--blue-deep);border-bottom:1.5px solid var(--blue-deep);transform:rotate(40deg)}
  .checks--front{font-size:8.6px;line-height:14.7px;padding:15px 10px 0 10px}
  .checks--back{font-size:8.6px;line-height:16.5px;padding:0 12px}
  .panel__title{font-family:"Dosis",sans-serif;font-weight:600;color:var(--yellow);font-size:12.5px;padding:9px 12px 3px}

  .badge{position:absolute;left:380px;top:189px;width:98px;height:98px;border-radius:50%;background:var(--yellow);border:3px solid #fff;box-shadow:0 1px 4px rgba(0,0,0,.3);display:flex;align-items:center;justify-content:center;text-align:center;font-family:"Dosis",sans-serif;font-weight:700;color:var(--blue-deep);font-size:17px;line-height:1.18}

  .redfield{position:absolute;left:238px;top:74px;width:261px;height:507px;background:linear-gradient(180deg,var(--red),var(--red-deep))}

  .footer{position:absolute;left:0;bottom:0;width:499px;height:52px;background:var(--red);display:flex;align-items:center;padding-left:27px;color:#fff}
  .footer__call{font-family:"Dosis",sans-serif;font-weight:600;font-size:15px;width:243px}
  .footer__icon{width:20px;height:20px;margin-right:10px}
  .footer__phone{font-family:"Dosis",sans-serif;font-weight:700;color:var(--yellow);font-size:31px;letter-spacing:.3px}
</style>
</head>
<body>

<section class="sheet sheet--front" aria-label="Brisk Chill line card, front">
  <svg class="art" width="499" height="645" viewBox="0 0 499 645">
    <defs>
      <linearGradient id="heroFade" x1="0" y1="0" x2="0" y2="1">
        <stop offset="0" stop-color="#f4f4f4"/>
        <stop offset=".22" stop-color="#c9a94a"/>
        <stop offset=".6" stop-color="#7a6a4a"/>
        <stop offset="1" stop-color="#4a3f33"/>
      </linearGradient>
    </defs>
    <rect x="0" y="60" width="499" height="250" fill="url(#heroFade)" role="img" aria-label="Photo of a yellow chiller unit inside a trailer beside a red shipping container"/>
    <path d="M0,236 C110,282 230,300 330,270 C410,246 460,215 499,180 V645 H0 Z" fill="var(--red)"/>
    <path d="M0,262 C110,300 230,312 330,286 C410,264 460,236 499,210 V645 H0 Z" fill="var(--paper)"/>
  </svg>

  <div class="brand" style="left:27px;top:25px"><span class="brand__dot"></span><span>Mobile Breeze<br>and Volt</span></div>
  <div class="tagline" style="right:19px;top:30px">
    <div class="tagline__services">Rental • Sales • Service</div>
    <div class="tagline__url">www.mobilebreezeandvolt.com</div>
  </div>

  <div class="badge">BRISK<br>CHILL<br>EQUIPMENT</div>

  <div class="panel" style="left:293px;top:284px;width:194px;height:183px">
    <ul class="checks checks--front">
      <li>24/7 Rapid Response</li>
      <li>Nationwide Service Area</li>
      <li>Unparalleled Customer Service</li>
      <li>Over 25 years of experience in HVAC and power</li>
      <li>Customization of equipment to meet individual customer needs</li>
      <li>Delivery &amp; installation of all equipment</li>
      <li>Extensive fleet inventory</li>
      <li>Trailers up to 48' long</li>
    </ul>
  </div>

  <div class="tab" style="left:0;top:313px;width:180px">BRISK - CHILL</div>

  <ul class="bullets" style="left:27px;top:351px;width:242px">
    <li>Brisk Chill is the process or technique of arresting the ripening of fruits and vegetables after harvesting by immersion of ice or cold water.</li>
    <li>Fruits and vegetables can be cooled rapidly by bringing them in contact with cold moving water.</li>
  </ul>

  <div class="photo photo--crates" style="left:23px;top:435px;width:114px;height:74px" role="img" aria-label="Photo of produce crates stacked in a trailer"></div>
  <div class="photo photo--trailer" style="left:146px;top:435px;width:114px;height:74px" role="img" aria-label="Photo of a trailer side with hoses at a loading dock"></div>
  <div class="photo photo--dock" style="left:23px;top:514px;width:114px;height:71px" role="img" aria-label="Photo of a trailer backed up to a red container"></div>
  <div class="photo photo--hose" style="left:146px;top:514px;width:114px;height:71px" role="img" aria-label="Photo of a cooling hose inside a loaded trailer"></div>

  <div class="equip equip--chiller" style="left:287px;top:480px;width:187px;height:102px" role="img" aria-label="Image of a yellow air-cooled chiller unit"></div>

  <div class="footer">
    <span class="footer__call">CALL FOR YOUR QUOTE TODAY</span>
    <svg class="footer__icon" viewBox="0 0 20 20" aria-hidden="true"><circle cx="10" cy="10" r="8.5" fill="none" stroke="var(--yellow)" stroke-width="1.6"/><path d="M7 5.5l1.6 2.2-1 1.1c.6 1.3 1.4 2.1 2.6 2.6l1.1-1 2.2 1.6-.9 1.8c-3.3-.2-6.3-3.2-6.5-6.5z" fill="var(--yellow)"/></svg>
    <span class="footer__phone">888-472-1086</span>
  </div>
</section>

<section class="sheet sheet--back" aria-label="Brisk Chill line card, back">
  <div class="brand" style="left:20px;top:22px"><span class="brand__dot"></span><span>Mobile Breeze<br>and Volt</span></div>
  <div class="tagline" style="right:32px;top:26px">
    <div class="tagline__services">Rental • Sales • Service</div>
    <div class="tagline__url">www.mobilebreezeandvolt.com</div>
  </div>

  <div class="redfield"></div>
  <div class="tab" style="left:238px;top:90px;width:180px">PRODUCT BENEFITS</div>

  <ul class="bullets bullets--light" style="left:250px;top:126px;width:237px">
    <li>Brisk Chill does not remove water from the product and can even revive slightly wilted produce.</li>
    <li>Brisk Chill increases shelf life through temperature control of fresh produce &amp; helps with flavor retention.</li>
    <li>Brisk Chill helps ensure product quality retention: temperature and humidity control in post harvest help prevent tissue damage and promote shelf life.</li>
    <li>Brisk Chill controls field temperatures, which prevents extreme product weight loss caused by dehydration.</li>
    <li>Brisk Chill is one of the fastest pre-cooling methods: when temperature rises, respiration and heat generation also increase, which decreases shelf time.</li>
    <li>Brisk Chill allows fruit to be showered with water to avoid "channeling" (water pouring through larger openings where there is less resistance).</li>
  </ul>

  <div class="photo photo--trailer" style="left:22px;top:90px;width:182px;height:110px" role="img" aria-label="Photo of a trailer at a loading dock next to a red container"></div>
  <div class="photo photo--carrots" style="left:22px;top:218px;width:182px;height:108px" role="img" aria-label="Photo of carrots being cooled under running water"></div>

  <div class="panel" style="left:22px;top:336px;width:463px;height:128px">
    <div class="panel__title">MOBILE BREEZE AND VOLT EQUIPMENT BENEFITS</div>
    <ul class="checks checks--back">
      <li>Brisk Chill equipment is 15x faster than air, allowing for increased production and labor savings.</li>
      <li>Brisk Chill equipment is 30% more efficient than air, resulting in power consumption savings.</li>
      <li>Brisk Chill equipment- our systems are more flexible and can be designed and installed on large and small scales.</li>
      <li>Brisk Chill equipment: Can be used with various packaging options.</li>
    </ul>
  </div>

  <div class="photo photo--load" style="left:22px;top:474px;width:182px;height:101px" role="img" aria-label="Photo of produce boxes in a trailer with cooling hoses"></div>
  <div class="equip equip--trailer" style="left:250px;top:472px;width:232px;height:109px" role="img" aria-label="Image of two yellow trailer-mounted generator units"></div>

  <div class="footer">
    <span class="footer__call">CALL FOR YOUR QUOTE TODAY</span>
    <svg class="footer__icon" viewBox="0 0 20 20" aria-hidden="true"><circle cx="10" cy="10" r="8.5" fill="none" stroke="var(--yellow)" stroke-width="1.6"/><path d="M7 5.5l1.6 2.2-1 1.1c.6 1.3 1.4 2.1 2.6 2.6l1.1-1 2.2 1.6-.9 1.8c-3.3-.2-6.3-3.2-6.5-6.5z" fill="var(--yellow)"/></svg>
    <span class="footer__phone">888-472-1086</span>
  </div>
</section>

</body>
</html>
```